Law Firm Stationery Design - Traditional Meets Intuitive

Looking for a modern, yet classic, law firm stationery design. Simplicity is desired, but great ideas are encouraged. See attachment for company information. We utilize a variety of non-traditional legal tools to bring a different perspective to each of our client's particular situation. Final design should communicate classic values with intuitive, unique solutions.

Industry/Entity Type

Law Firm

Requirements
Should not have
• - No typical legal icons
• - No Tag Line!
• - DO NOT WANT WHAT WE ALREADY HAVE

```html
<!DOCTYPE html>
<html lang="en">
<head>
<meta charset="utf-8">
<title>Veranth Law LLC Stationery</title>
<link href="https://fonts.googleapis.com/css2?family=Crimson+Text:wght@400;600&display=swap" rel="stylesheet">
<style>
  :root {
    --backdrop: #b5b5b5;
    --paper: #ffffff;
    --ink: #231f20;
    --shadow: rgba(0, 0, 0, 0.35);
  }
  * { box-sizing: border-box; margin: 0; padding: 0; }
  html, body {
    width: 1200px; height: 2387px; overflow: hidden;
    background: var(--backdrop);
    font-family: "Crimson Text", Georgia, serif;
    color: var(--ink);
  }
  .canvas { position: relative; width: 1200px; height: 2387px; }
  .sheet {
    position: absolute; background: var(--paper);
    box-shadow: 2px 4px 10px var(--shadow);
  }
  .letterhead-back { left: 72px; top: 88px; width: 915px; height: 1185px; }
  .letterhead-front { left: 212px; top: 275px; width: 917px; height: 1186px; }
  .envelope { left: 88px; top: 1552px; width: 1023px; height: 442px; }
  .card-back { left: 200px; top: 2083px; width: 377px; height: 215px; }
  .card-front { left: 622px; top: 2083px; width: 377px; height: 215px; }

  .firm-name {
    position: absolute; font-weight: 600; letter-spacing: 1px;
    font-size: 46px; line-height: 1; white-space: nowrap;
  }
  .letterhead-back .firm-name { left: 48px; top: 80px; }
  .letterhead-front .firm-name { left: 290px; top: 66px; }
  .envelope .firm-name { left: 24px; top: 30px; }
  .card-front .firm-name { left: 62px; top: 86px; font-size: 30px; }

  .contact {
    position: absolute; border-left: 2px solid var(--ink);
    padding-left: 14px; font-size: 11px; line-height: 15px;
  }
  .letterhead-back .contact { left: 719px; top: 62px; }
  .letterhead-front .contact { left: 719px; top: 1093px; }
  .card-back .contact { left: 189px; top: 136px; font-size: 10px; line-height: 13.5px; padding-left: 12px; }

  .return-address {
    position: absolute; left: 24px; top: 107px;
    font-size: 11px; line-height: 15px;
  }
  .holder-name {
    position: absolute; left: 58px; top: 168px;
    font-size: 12.5px; font-weight: 600; letter-spacing: 0.6px;
  }
</style>
</head>
<body>
<main class="canvas">
  <section class="sheet letterhead-back">
    <div class="firm-name">VERANTH LAW LLC</div>
    <address class="contact">
      18 Harbor Lane, Suite 300<br>
      Easton, MA 02375<br>
      555-010-4000<br>
      info@veranthlaw.com<br>
      www.veranthlaw.com
    </address>
  </section>

  <section class="sheet letterhead-front">
    <div class="firm-name">VERANTH LAW LLC</div>
    <address class="contact">
      18 Harbor Lane, Suite 300<br>
      Easton, MA 02375<br>
      555-010-4000<br>
      info@veranthlaw.com<br>
      www.veranthlaw.com
    </address>
  </section>

  <section class="sheet envelope">
    <div class="firm-name">VERANTH LAW LLC</div>
    <address class="return-address">
      18 Harbor Lane, Suite 300<br>
      Easton, MA 02375
    </address>
  </section>

  <section class="sheet card-back">
    <div class="holder-name">DANIEL R. MOREAU</div>
    <address class="contact">
      18 Harbor Lane, Suite 300<br>
      Easton, MA 02375<br>
      555-010-4000<br>
      info@veranthlaw.com<br>
      www.veranthlaw.com
    </address>
  </section>

  <section class="sheet card-front">
    <div class="firm-name">VERANTH LAW LLC</div>
  </section>
</main>
</body>
</html>
```